PELDRAX Business Cards

We require a business card for our company that provides IT consulting services. We already have a logo that needs to be used on the card. We want a clean professional looking design that incorporates our colours. Our main focus is providing managed services to business, which involves us looking after all of their IT requirements including managing servers/networks, projects, and procurement.

Industry/Entity Type

Information Technology

Requirements
Must have
• our logo, contact information, name, title, phone numbers

```html
<!DOCTYPE html>
<html lang="en">
<head>
<meta charset="UTF-8">
<title>PELDRAX Business Cards</title>
<link rel="stylesheet" href="https://fonts.googleapis.com/css2?family=Montserrat:wght@500;600&family=Work+Sans:wght@400;500&display=swap">
<style>
  :root {
    --brand-blue: #1592cf;
    --card-white: #ffffff;
    --backdrop: #e4e6e9;
    --ink-light: #ffffff;
  }
  * { margin: 0; padding: 0; box-sizing: border-box; }
  html, body { width: 1200px; height: 800px; overflow: hidden; }
  body {
    background: var(--backdrop);
    font-family: "Work Sans", sans-serif;
    position: relative;
  }
  .card {
    position: absolute;
    top: 245px;
    width: 540px;
    height: 310px;
    border-radius: 18px;
    overflow: hidden;
    box-shadow: 0 10px 28px rgba(0,0,0,0.18);
  }
  .card-front { left: 40px; background: var(--card-white); }
  .card-back { left: 620px; background: var(--brand-blue); }

  .front-panel { position: absolute; inset: 0; }

  .wordmark {
    font-family: "Montserrat", sans-serif;
    font-weight: 600;
    letter-spacing: 0.08em;
    position: absolute;
    display: flex;
    align-items: center;
    gap: 12px;
  }
  .wordmark-dot {
    border-radius: 50%;
    flex-shrink: 0;
  }
  .front-wordmark {
    left: 38px;
    top: 82px;
    font-size: 36px;
    color: var(--brand-blue);
  }
  .front-wordmark .wordmark-dot { width: 30px; height: 30px; background: var(--brand-blue); }

  .contact-block {
    position: absolute;
    left: 322px;
    top: 46px;
    color: var(--ink-light);
  }
  .person-name {
    font-family: "Montserrat", sans-serif;
    font-weight: 600;
    font-size: 23px;
    letter-spacing: 0.1em;
  }
  .person-title {
    font-size: 13px;
    margin-top: 2px;
  }
  .address {
    font-size: 12px;
    line-height: 1.35;
    margin-top: 16px;
    letter-spacing: 0.03em;
  }
  .contact-list {
    list-style: none;
    margin-top: 16px;
    font-size: 12.5px;
    line-height: 1.5;
    letter-spacing: 0.02em;
  }
  .contact-list li { display: flex; align-items: center; gap: 9px; }
  .contact-list svg { width: 11px; height: 11px; flex-shrink: 0; }
  .contact-list .site { font-weight: 500; }

  .back-wordmark {
    left: 50%;
    top: 112px;
    transform: translateX(-50%);
    font-size: 48px;
    color: var(--ink-light);
  }
  .back-wordmark .wordmark-dot { width: 40px; height: 40px; background: var(--ink-light); }
  .back-site {
    position: absolute;
    left: 0; right: 0;
    top: 200px;
    text-align: center;
    color: var(--ink-light);
    font-size: 17px;
    letter-spacing: 0.06em;
  }
</style>
</head>
<body>
  <section class="card card-front" aria-label="Business card front">
    <svg class="front-panel" viewBox="0 0 540 310" width="540" height="310" aria-hidden="true">
      <path d="M300 0 H540 V310 H228 L300 160 V86 L292 78 L300 70 Z" fill="#1592cf"/>
    </svg>
    <div class="wordmark front-wordmark"><span class="wordmark-dot"></span>PELDRAX</div>
    <div class="contact-block">
      <h1 class="person-name">MORGAN HALE</h1>
      <p class="person-title">CEO/Founder</p>
      <p class="address">2740 Harbor Crest Road,<br>Port Alden,<br>Florida, 34902</p>
      <ul class="contact-list">
        <li><svg viewBox="0 0 12 12"><rect x="3" y="0.5" width="6" height="11" rx="1" fill="none" stroke="#fff"/><circle cx="6" cy="9.5" r="0.7" fill="#fff"/></svg>(555) 318-4402</li>
        <li><svg viewBox="0 0 12 12"><path d="M2.5 1 L4.5 1 L5.2 3.6 L4 4.6 Q5 7 7.4 8 L8.4 6.8 L11 7.5 V9.5 Q10 11 8 11 Q1 9 1 3 Q1 1.5 2.5 1 Z" fill="#fff"/></svg>1-800-555-0147 (Toll Free)</li>
        <li><svg viewBox="0 0 12 12"><rect x="0.5" y="2" width="11" height="8" fill="none" stroke="#fff"/><path d="M0.5 2 L6 6.5 L11.5 2" fill="none" stroke="#fff"/></svg>info@peldrax.com</li>
        <li><svg viewBox="0 0 12 12"><circle cx="6" cy="6" r="5.3" fill="none" stroke="#fff"/><ellipse cx="6" cy="6" rx="2.3" ry="5.3" fill="none" stroke="#fff"/><path d="M0.7 6 H11.3" stroke="#fff"/></svg><span class="site">www.peldrax.com</span></li>
      </ul>
    </div>
  </section>

  <section class="card card-back" aria-label="Business card back">
    <div class="wordmark back-wordmark"><span class="wordmark-dot"></span>PELDRAX</div>
    <p class="back-site">www.peldrax.com</p>
  </section>
</body>
</html>
```